Truck wrap Halvik T-720 as a rolling billboard

have multiple trucks to wrap with logo and company info as a rolling billboard.

Tarnwell Outfitters logo

Main focus are in sod

contact 555-317-4486

licensed and insured - maybe on back of truck
"Sod and Landscape Installation and Delivery" - on side of truck

Target Market(s)

landscapers and builders

Industry/Entity Type

Landscape

Font styles to use
Sans Serif

Colors
acd037

Requirements
Must have
• photo of palletized sod
555-317-4486
Nice to have
• cool way to show palletized sod

Quenlar logo that can be added or taken away from deisgn
Should not have
• no big leaf
Sod needs to be bigger than the leaf from the logo

```html
<!DOCTYPE html>
<html lang="en">
<head>
<meta charset="utf-8">
<title>Tarnwell Outfitters – Halvik T-720 wrap</title>
<link rel="stylesheet" href="https://fonts.googleapis.com/css2?family=Montserrat:wght@700;800&display=swap">
<style>
  :root {
    --canvas: #eef0ec;
    --body: #ffffff;
    --outline: #3d4650;
    --glass: #96c9c9;
    --trim: #3f4a56;
    --flare: #33383e;
    --tire: #2b2f33;
    --rim: #c9ced3;
    --lamp: #e9863a;
    --brand-green: #8ab511;
    --brand-gold: #d9a300;
    --text-light: #ffffff;
  }
  html, body {
    margin: 0;
    padding: 0;
    width: 1096px;
    height: 1200px;
    overflow: hidden;
    background: var(--canvas);
  }
  .wrap-sheet { display: block; width: 1096px; height: 1200px; }
  .truck-body { fill: var(--body); stroke: var(--outline); stroke-width: 3; }
  .panel-line { stroke: var(--outline); stroke-width: 3; fill: none; }
  .window { fill: var(--glass); stroke: var(--outline); stroke-width: 3; }
  .pillar, .handle, .mirror, .grille-guard, .frame-rail { fill: var(--trim); }
  .fender-flare { fill: var(--flare); }
  .wheel-well { fill: #1f2226; }
  .head-lamp { fill: var(--lamp); }
  .tire { fill: var(--tire); }
  .rim { fill: var(--rim); }
  .hub { fill: #8d949b; }
  .accent-band { fill: var(--brand-gold); }
  .main-band { fill: var(--brand-green); }
  .sod-photo { fill: url(#sodTones); stroke: var(--brand-green); stroke-width: 9; }
  .brand-name {
    font-family: "Montserrat", sans-serif;
    font-weight: 800;
    fill: var(--brand-green);
    font-size: 46px;
    letter-spacing: 1px;
  }
  .brand-dot { fill: var(--brand-green); }
  .phone {
    font-family: "Montserrat", sans-serif;
    font-weight: 800;
    font-size: 62px;
    fill: var(--text-light);
  }
  .service {
    font-family: "Montserrat", sans-serif;
    font-weight: 800;
    font-size: 30px;
    fill: var(--text-light);
  }
  .service-dot { fill: var(--text-light); }
</style>
</head>
<body>
<svg class="wrap-sheet" viewBox="0 0 1786 1954" xmlns="http://www.w3.org/2000/svg">
  <defs>
    <linearGradient id="sodTones" x1="0" y1="0" x2="1" y2="1">
      <stop offset="0" stop-color="#6fb83a"/>
      <stop offset="0.45" stop-color="#5a8a2c"/>
      <stop offset="1" stop-color="#8a6a3f"/>
    </linearGradient>

    <g id="truckSide">
      <rect class="frame-rail" x="1690" y="40" width="96" height="680" rx="12"/>
      <path class="truck-body" d="M135,358 C200,322 400,292 560,276 L640,262 C720,170 800,100 880,78 L1740,62 C1770,62 1780,85 1780,110 L1780,700 L135,700 Z"/>
      <rect class="frame-rail" x="640" y="700" width="1140" height="18"/>
      <path class="window" d="M870,97 L1185,97 L1185,347 L910,352 C880,345 858,330 852,310 Z"/>
      <rect class="pillar" x="1185" y="97" width="105" height="215"/>
      <path class="window" d="M1290,97 L1580,97 C1600,100 1605,120 1605,140 L1605,270 C1570,295 1520,305 1290,310 Z"/>
      <path class="mirror" d="M795,195 L850,190 C865,200 868,230 866,260 L865,345 L790,345 C780,300 782,230 795,195 Z"/>
      <path class="panel-line" d="M710,360 L710,700 M1238,97 L1238,700 M700,355 L1780,355"/>

      <path class="accent-band" d="M200,372 C300,356 560,350 640,420 C700,480 720,530 760,545 C900,578 1050,545 1200,545 C1400,545 1500,600 1700,560 L1700,683 Q1700,705 1678,705 L720,705 C705,540 600,440 440,440 C320,440 225,480 200,525 Z"/>
      <path class="main-band" d="M200,390 C300,374 560,368 635,437 C695,497 720,546 760,561 C900,594 1050,561 1200,561 C1400,561 1500,616 1700,576 L1700,683 Q1700,705 1678,705 L720,705 C705,540 600,440 440,440 C320,440 225,480 200,525 Z"/>

      <path class="fender-flare" d="M190,720 L190,560 C225,478 320,440 440,440 C600,440 705,540 720,705 L720,720 Z"/>
      <path class="wheel-well" d="M225,720 C230,545 330,480 440,480 C575,480 672,560 680,720 Z"/>
      <rect class="grille-guard" x="30" y="345" width="165" height="370" rx="30"/>
      <rect class="head-lamp" x="155" y="385" width="40" height="70" rx="6"/>

      <circle class="tire" cx="415" cy="765" r="172"/>
      <circle class="rim" cx="415" cy="765" r="98"/>
      <circle class="hub" cx="415" cy="765" r="40"/>
      <circle class="tire" cx="415" cy="765" r="20"/>

      <path class="sod-photo" role="img" aria-label="Photo of a stacked pallet of fresh sod" d="M1258,375 C1380,356 1520,360 1570,378 C1600,480 1560,605 1450,636 L1310,636 C1265,560 1248,460 1258,375 Z"/>
      <rect class="handle" x="1120" y="385" width="90" height="32" rx="8"/>
      <rect class="handle" x="1545" y="385" width="90" height="32" rx="8"/>
    </g>
  </defs>

  <g class="truck driver-side">
    <use href="#truckSide"/>
    <circle class="brand-dot" cx="775" cy="470" r="22"/>
    <text class="brand-name" x="812" y="466">TARNWELL</text>
    <text class="brand-name" x="812" y="518">OUTFITTERS</text>
    <text class="phone" x="968" y="624" text-anchor="middle">555-317-4486</text>
    <g class="services">
      <text class="service" x="742" y="672">SOD</text>
      <circle class="service-dot" cx="846" cy="661" r="9"/>
      <text class="service" x="876" y="672">LANDSCAPE</text>
      <circle class="service-dot" cx="1121" cy="661" r="9"/>
      <text class="service" x="1146" y="672">INSTALLATION</text>
      <circle class="service-dot" cx="1426" cy="661" r="9"/>
      <text class="service" x="1452" y="672">DELIVERY</text>
    </g>
  </g>

  <g class="truck passenger-side">
    <use href="#truckSide" transform="translate(1786,977) scale(-1,1)"/>
    <circle class="brand-dot" cx="625" cy="1447" r="22"/>
    <text class="brand-name" x="662" y="1443">TARNWELL</text>
    <text class="brand-name" x="662" y="1495">OUTFITTERS</text>
    <text class="phone" x="818" y="1601" text-anchor="middle">555-317-4486</text>
    <g class="services">
      <text class="service" x="158" y="1652">SOD</text>
      <circle class="service-dot" cx="262" cy="1641" r="9"/>
      <text class="service" x="292" y="1652">LANDSCAPE</text>
      <circle class="service-dot" cx="537" cy="1641" r="9"/>
      <text class="service" x="562" y="1652">INSTALLATION</text>
      <circle class="service-dot" cx="842" cy="1641" r="9"/>
      <text class="service" x="868" y="1652">DELIVERY</text>
    </g>
  </g>
</svg>
</body>
</html>
```